A hand soap seller needs a premium label for a new product

We need a premium label for a bottle of soap. We want to write on it:
VANTROSELLA (Name)
Hypoallergenic and antibacterial hand soap
350 ml e / 11.8 fl oz (volume, http://pimaxo.ru/7K3RtWbqmeL519)
Saint Petersburg - Russia / www.vantrosella.ru
We want to see the face of a hippopotamus in the design. Use only black and white and green for accents (the color of grass). Examples of a hippopotamus are shown in the photo. Our soap is hypoallergenic. Ideal for both children and adults. Therefore, the label should appeal to adults and children.
The bottle will be white, and the soap dispenser will be black.
So I'm attaching an example of a soap design that we liked
Label size: height-78 mm, width-102 mm !!!

Target Market(s)

Mothers and children

Industry/Entity Type

Hand soap

Font styles to use
Serif

Colors

Designer to choose only greyscale colors for use in the design.

Requirements
Must have
• The face of a hippopotamus emerging from the grass, Black and white palette with elements of green (grass color)
Nice to have
• The face of a hippopotamus emerging from the grass
Should not have
• Different colors

```html
<!DOCTYPE html>
<html lang="en">
<head>
<meta charset="utf-8">
<title>Vantrosella Hypoallergenic Hand Soap Label</title>
<link href="https://fonts.googleapis.com/css2?family=Amatic+SC:wght@400;700&display=swap" rel="stylesheet">
<style>
  :root {
    --paper: #ffffff;
    --label-green: #6ab198;
    --mint: #b1dece;
    --ink-light: #ffffff;
  }
  html, body {
    margin: 0;
    padding: 0;
    overflow: hidden;
    background: var(--paper);
  }
  .canvas {
    position: relative;
    width: 1200px;
    height: 1174px;
    background: var(--paper);
    overflow: hidden;
    font-family: "Amatic SC", sans-serif;
    color: var(--ink-light);
  }
  .label {
    position: absolute;
    left: 249px;
    top: 133px;
    width: 702px;
    height: 908px;
    background: var(--label-green);
    border-radius: 284px / 286px;
  }
  .brand-arc {
    position: absolute;
    left: 0;
    top: 0;
    width: 1200px;
    height: 1174px;
    pointer-events: none;
  }
  .brand-arc text {
    font-family: "Amatic SC", sans-serif;
    font-weight: 400;
    font-size: 92px;
    letter-spacing: 14px;
    fill: var(--ink-light);
  }
  .mascot-art {
    position: absolute;
    left: 485px;
    top: 283px;
    width: 232px;
    height: 276px;
    border-radius: 46% 46% 40% 40% / 38% 38% 34% 34%;
    background: linear-gradient(180deg, var(--label-green) 0%, var(--label-green) 40%, var(--mint) 40%, var(--mint) 100%);
    border: 4px solid var(--ink-light);
    box-sizing: border-box;
  }
  .product-type {
    position: absolute;
    left: 0;
    width: 1200px;
    margin: 0;
    text-align: center;
    font-weight: 400;
    line-height: 1;
  }
  .product-type--main {
    top: 578px;
    font-size: 76px;
    letter-spacing: 19px;
    text-indent: 19px;
  }
  .product-type--sub {
    top: 684px;
    font-size: 68px;
    letter-spacing: 20px;
    text-indent: 20px;
  }
  .volume {
    position: absolute;
    left: 0;
    top: 870px;
    width: 1200px;
    margin: 0;
    text-align: center;
    font-size: 34px;
    font-weight: 700;
    letter-spacing: 6px;
    line-height: 1;
  }
</style>
</head>
<body>
<main class="canvas">
  <section class="label">
  </section>

  <svg class="brand-arc" viewBox="0 0 1200 1174" aria-label="VANTROSELLA">
    <defs>
      <path id="brand-curve" d="M 235 602 A 365 365 0 0 1 965 602"/>
    </defs>
    <text>
      <textPath href="#brand-curve" startOffset="50%" text-anchor="middle">VANTROSELLA</textPath>
    </text>
  </svg>

  <div class="mascot-art" role="img" aria-label="Cartoon hippopotamus head illustration in green and mint with white outline"></div>

  <h1 class="product-type product-type--main">HYPOALLERGENIC</h1>
  <h2 class="product-type product-type--sub">HAND SOAP</h2>

  <p class="volume">350 ml e / 11.8 fl oz</p>
</main>
</body>
</html>
```